Letterhead Design for Law Firm that Specializes in Property Damage Litigation

We are looking for a redesign of our letterhead. Our current letterhead lists all of our current staff members and we'd like to come up with a design that does NOT list all of the staff members so that it does not need to be updated with every newly hired employee. Must be in editable format.

We are a law firm that specializes in property damage, so we need something that is professional, yet modern. The final design should use our existing logo and should use a blue color scheme (alternate colors would be gray, black, and white).

Industry/Entity Type

Legal

Colors
0054AA
0677BA
7BADD7
CADEEF
E8F1F8

```html
<!DOCTYPE html>
<html lang="en">
<head>
<meta charset="utf-8">
<title>Hartwell Crane &amp; Osborne — Letterhead</title>
<link href="https://fonts.googleapis.com/css2?family=Montserrat:ital,wght@0,400;0,500;0,600;0,700;1,300&display=swap" rel="stylesheet">
<style>
  :root {
    --navy: #00315f;
    --slate: #666666;
    --ink: #1a1a1a;
    --muted: #5c5c5c;
    --paper: #ffffff;
    --backdrop: #ededed;
  }
  * { box-sizing: border-box; margin: 0; padding: 0; }
  html, body {
    width: 1200px; height: 1057px; overflow: hidden;
    background: var(--backdrop);
    font-family: "Montserrat", sans-serif;
  }
  .letterhead {
    position: absolute; left: 308px; top: 116px;
    width: 583px; height: 825px;
    background: var(--paper);
    overflow: hidden;
  }
  .accent-bar {
    position: absolute; left: 0; top: 33px;
    width: 11px; height: 111px;
    background: var(--navy);
  }
  .brand {
    position: absolute; left: 31px; top: 56px;
  }
  .brand-mark {
    display: flex; align-items: center; gap: 8px;
  }
  .brand-square {
    width: 14px; height: 14px; background: var(--navy);
  }
  .brand-name {
    font-weight: 700; font-size: 15px; line-height: 17px;
    color: var(--navy); letter-spacing: 0.04em; text-transform: uppercase;
  }
  .brand-tagline {
    margin-top: 10px;
    font-size: 6.4px; font-weight: 600; letter-spacing: 0.18em;
    color: var(--slate); text-transform: uppercase;
  }
  .letter {
    position: absolute; left: 66px; top: 202px; width: 452px;
  }
  .letter-body {
    font-size: 11.4px; line-height: 16.3px; color: var(--ink);
    text-align: justify; word-spacing: -0.4px;
  }
  .letter-body p + p { margin-top: 16.3px; }
  .letter-body p.run-on { margin-top: 0; }
  .signature {
    margin-top: 15px;
    line-height: 13px;
  }
  .signature-name { font-weight: 600; font-size: 12.4px; color: #000; }
  .signature-role { font-style: italic; font-weight: 300; font-size: 12px; color: var(--ink); }
  .contact {
    position: absolute; left: 31px; top: 683px;
    font-size: 10.4px; line-height: 19.4px; color: var(--muted);
    list-style: none;
  }
  .contact .street { font-weight: 700; }
  .footer-band {
    position: absolute; left: 0; bottom: 0; width: 583px; height: 41px;
  }
</style>
</head>
<body>
  <main class="letterhead">
    <div class="accent-bar"></div>

    <header class="brand">
      <div class="brand-mark">
        <span class="brand-square"></span>
        <span class="brand-name">Hartwell Crane<br>&amp; Osborne</span>
      </div>
      <p class="brand-tagline">The Property Damage Attorneys</p>
    </header>

    <article class="letter">
      <section class="letter-body">
        <p>Lorem ipsum dolor sit amet. Eos gubergren assum tempor autem. Sit ipsum odio diam. Vero dolore sea aliquip voluptua nonumy. Labore lorem molestie sed est. Sed sea tempor labore amet lorem vel soluta. Takimata accumsan blandit diam et. Soluta ut ullamcorper diam voluptua augue zzril. Justo sed erat. Ea wisi est et. Et vel sadipscing.</p>
        <p>Est sea zzril elitr amet. Magna ipsum dolor et suscipit nihil. Duis erat consectetuer in aliquyam in. Et sea amet gubergren. Vel assum liber ea cum vero diam. Et facilisis euismod option tempor ut. Duo accumsan dolor. In elitr duo et eu sit invidunt lorem. Et facilisis ea duis zzril takimata minim quis. Diam dolore nonumy sit. Enim aliquyam sanctus facilisis elitr. Justo ea diam sea lorem diam et. Ut duis amet eos te voluptua vulputate lobortis. Consetetur ea justo magna lorem et.</p>
        <p class="run-on">Dolor vulputate takimata. Amet euismod dolore takimata vero erat ipsum. Vulputate lorem magna euismod nostrud takimata nulla iriure. Justo vero et. Amet iriure vero. Adipiscing takimata nisl rebum ipsum. Id takimata erat elit nihil luptatum. Ipsum consetetur eu. Tempor eirmod facilisis lorem dignissim. Sed justo ea at et nonumy gubergren invidunt. Sanctus lorem sanctus velit.</p>
        <p>Dolor vulputate takimata. Amet euismod dolore takimata vero erat ipsum. Vulputate lorem magna euismod nostrud takimata nulla iriure. Justo vero et. Amet iriure vero. Adipiscing takimata nisl rebum ipsum. Id takimata erat elit nihil luptatum. Ipsum consetetur eu. Tempor eirmod facilisis lorem dignissim. Sed justo ea at et nonumy gubergren invidunt. Sanctus lorem sanctus velit.</p>
      </section>

      <div class="signature">
        <p class="signature-name">Your Name</p>
        <p class="signature-role">Position</p>
      </div>
    </article>

    <ul class="contact">
      <li class="street">2240 Market Street, Suite 840</li>
      <li>Riverton, PA 19077</li>
      <li>Phone: (215) 555-0142</li>
      <li>Fax: (215) 555-0187</li>
    </ul>

    <svg class="footer-band" viewBox="0 0 583 41" aria-hidden="true">
      <rect x="0" y="16" width="583" height="25" fill="var(--slate)"/>
      <polygon points="0,0 244,0 276,41 0,41" fill="var(--navy)"/>
    </svg>
  </main>
</body>
</html>
```